Business Card Design Project

We would like a business card designed for our Tiny Acorns Club. Although we do want to be creative, it is important for us to maintain branding, therefore most of the design will be copied from our website.
We do want people to know what it is all about, so we included some of the wording. However we rely heavily on your advice and if you think it is better without then as long as design is good we are willing to consider it.
All designs submitted must follow print-ready design rules. Use only CMYK colours
Target Market(s)
Mothers and mothers-to-be
Industry/Entity Type
Business
Look and feel
Each slider illustrates characteristics of the customer's brand and the style your logo design should communicate.

```html
<!DOCTYPE html>
<html lang="en">
<head>
<meta charset="utf-8">
<title>Tiny Acorns Club – Business Card</title>
<link rel="stylesheet" href="https://fonts.googleapis.com/css2?family=Sorts+Mill+Goudy&family=Ubuntu:wght@400;500;700&display=swap">
<style>
  :root {
    --band-light: #fbb12a;
    --band-dark: #f39a1c;
    --label: #fbbf1c;
    --title-ink: #4d3f1e;
    --accent: #f0921f;
    --footer-ink: #1f1f1f;
    --paper: #ffffff;
    --envelope: #c9c9c9;
    --globe: #3b8fd6;
    --globe-light: #9fd0f5;
  }
  * { margin: 0; padding: 0; box-sizing: border-box; }
  html, body { width: 1200px; height: 667px; overflow: hidden; background: var(--paper); }
  .card {
    position: relative;
    width: 1200px;
    height: 667px;
    background: var(--paper);
    overflow: hidden;
    font-family: "Ubuntu", sans-serif;
  }
  .header-band {
    position: absolute;
    inset: 0 0 auto 0;
    height: 296px;
    background: linear-gradient(180deg, var(--band-light), var(--band-dark));
    box-shadow: 0 3px 5px rgba(90, 60, 0, .3);
  }
  .title-label {
    position: absolute;
    left: 34px;
    top: 45px;
    width: 1140px;
    height: 136px;
    background: var(--label);
    border-radius: 12px;
    box-shadow: 0 3px 5px rgba(110, 70, 0, .35);
    display: flex;
    align-items: center;
    justify-content: center;
  }
  .club-name {
    font-family: "Sorts Mill Goudy", serif;
    font-weight: 400;
    font-size: 78px;
    line-height: 1;
    color: var(--title-ink);
    padding-bottom: 4px;
  }
  .contact-person {
    position: absolute;
    top: 370px;
    left: 0;
    width: 100%;
    text-align: center;
    color: var(--accent);
    text-shadow: 1px 2px 3px rgba(0, 0, 0, .18);
  }
  .person-name { font-size: 76px; font-weight: 500; line-height: 1; }
  .person-phone { margin-top: 18px; font-size: 52px; font-weight: 500; line-height: 1; }
  .footer-links {
    position: absolute;
    top: 580px;
    left: 0;
    width: 100%;
    height: 52px;
  }
  .link {
    position: absolute;
    bottom: 0;
    height: 52px;
    display: flex;
    align-items: flex-end;
    gap: 12px;
    font-size: 16px;
    font-weight: 700;
    color: var(--footer-ink);
  }
  .link span { line-height: 1; padding-bottom: 4px; }
  .link--social { left: 50px; }
  .link--email { left: 429px; }
  .link--web { left: 864px; }
  .social-square {
    width: 48px; height: 48px;
    background: var(--accent);
    border-radius: 4px;
  }
  .footer-band {
    position: absolute;
    left: 0; bottom: 0;
    width: 100%;
    height: 29px;
    background: linear-gradient(180deg, var(--band-light), var(--band-dark));
  }
</style>
</head>
<body>
<main class="card">
  <header class="header-band">
    <div class="title-label">
      <h1 class="club-name">Tiny Acorns Club</h1>
    </div>
  </header>

  <section class="contact-person">
    <p class="person-name">Anna Reed</p>
    <p class="person-phone">1-800-555-0100</p>
  </section>

  <footer class="footer-links">
    <div class="link link--social">
      <div class="social-square"></div>
      <span>tinyacorns.club</span>
    </div>
    <div class="link link--email">
      <svg width="56" height="40" viewBox="0 0 56 40" aria-hidden="true">
        <rect x="1" y="1" width="54" height="38" rx="2" fill="#fafafa" stroke="var(--envelope)" stroke-width="2"/>
        <path d="M2 2 L28 24 L54 2 M2 38 L22 19 M54 38 L34 19" fill="none" stroke="var(--envelope)" stroke-width="2"/>
      </svg>
      <span>info@tinyacornsclub.com</span>
    </div>
    <div class="link link--web">
      <svg width="50" height="50" viewBox="0 0 50 50" aria-hidden="true">
        <circle cx="25" cy="25" r="23" fill="var(--globe)"/>
        <ellipse cx="25" cy="25" rx="11" ry="23" fill="none" stroke="var(--globe-light)" stroke-width="2"/>
        <path d="M2 25 H48 M6 13 H44 M6 37 H44" stroke="var(--globe-light)" stroke-width="2"/>
      </svg>
      <span>www.tinyacornsclub.com</span>
    </div>
  </footer>
  <div class="footer-band"></div>
</main>
</body>
</html>
```